Parfume Label

Hi
We are searching a design-label for our new parfume that we will launch soon.
The Brand of the company is http://www.marek-vosslin.ch/.
Please be aware that the label will be screen printed on a glass bottle.
The name of the parfume will be: Sea Glow
So for us its important that the name Sea Glow should be prominent on the label and the brand MAREK VOSSLIN only small to get the relation to the brand. To have same CI the name MAREK VOSSLIN should be written with our special font that i have attached. It also not necessary to put the MAREK VOSSLIN on a black background because with the screen print it will not look good.
For the Sea Glow you can use what ever you like, feel free to design.
In advance thanks for all designers that participate.
Have fun...

```html
<!DOCTYPE html>
<html lang="en">
<head>
<meta charset="utf-8">
<title>Sea Glow – Marek Vosslin perfume label</title>
<link rel="stylesheet" href="https://fonts.googleapis.com/css2?family=Rajdhani:wght@400;500&display=swap">
<style>
  :root {
    --ink-black: #000000;
    --board-light: #dcdcdc;
    --board-dark: #5e5e5e;
    --shelf-light: #e2e2e2;
    --label-yellow: #ffba00;
    --label-white: #ffffff;
    --glass-grey: #c9cbcb;
    --glass-amber: #d9c23a;
    --glass-aqua: #a9dbe6;
    --glass-base: #eef0f2;
  }
  html, body {
    margin: 0;
    padding: 0;
    overflow: hidden;
    background: var(--ink-black);
  }
  .board {
    position: relative;
    width: 1200px;
    height: 1200px;
    overflow: hidden;
    background: var(--ink-black);
    font-family: "Rajdhani", "Arial Narrow", sans-serif;
  }
  .board__backdrop {
    position: absolute;
    left: 0;
    top: 230px;
    width: 1200px;
    height: 515px;
    background: linear-gradient(to bottom, var(--board-light), var(--board-dark));
  }
  .board__shelf {
    position: absolute;
    left: 0;
    top: 745px;
    width: 1200px;
    height: 140px;
    background: linear-gradient(to bottom, var(--shelf-light) 0%, #bdbdbd 40%, var(--ink-black) 100%);
  }
  .label__bar {
    position: absolute;
    left: 118px;
    width: 553px;
    height: 94px;
    background: var(--label-yellow);
  }
  .label__bar--top { top: 303px; }
  .label__bar--brand {
    top: 717px;
    display: flex;
    align-items: center;
    justify-content: flex-end;
    padding-right: 19px;
    box-sizing: border-box;
  }
  .label__brand {
    color: var(--label-white);
    font-weight: 400;
    font-size: 54px;
    letter-spacing: 1px;
    line-height: 1;
    margin-top: 4px;
  }
  .label__name-area {
    position: absolute;
    left: 118px;
    top: 397px;
    width: 553px;
    height: 320px;
    padding-right: 19px;
    box-sizing: border-box;
    display: flex;
    align-items: center;
    justify-content: flex-end;
  }
  .label__name {
    margin: 0;
    color: var(--label-yellow);
    font-weight: 500;
    font-size: 128px;
    letter-spacing: 2px;
    line-height: 1;
    white-space: nowrap;
  }
  .bottle-photo {
    position: absolute;
    left: 732px;
    top: 303px;
    width: 368px;
    height: 509px;
    background: linear-gradient(to bottom,
      var(--glass-grey) 0%,
      var(--glass-grey) 36%,
      var(--glass-amber) 40%,
      var(--glass-amber) 56%,
      var(--glass-aqua) 60%,
      var(--glass-aqua) 86%,
      var(--glass-base) 92%,
      var(--glass-base) 100%);
  }
</style>
</head>
<body>
  <main class="board">
    <div class="board__backdrop"></div>
    <div class="board__shelf"></div>

    <section class="label" aria-label="Sea Glow label design">
      <div class="label__bar label__bar--top"></div>
      <div class="label__name-area">
        <h1 class="label__name">Sea Glow</h1>
      </div>
      <div class="label__bar label__bar--brand">
        <span class="label__brand">MAREK VOSSLIN</span>
      </div>
    </section>

    <div class="bottle-photo" role="img" aria-label="Photograph of a square glass perfume bottle with clear cap, filled with amber and aqua liquid, showing the Sea Glow label printed on the glass"></div>
  </main>
</body>
</html>
```